house and garden repairs and maintenance, bathroom repairs, painting inside and out, all outdoor lawns and gardens ,landscaping, spraying, lawn mowing cylinder or rotary

Industry/Entity Type

Painting

Contact Information for Business Card

tidy wren home and yard, repairs and maintenance inside and out mark 0427361508 dean 0439682715

Colors

Designer to choose colors to be used in the design.

```html
<!DOCTYPE html>
<html lang="en">
<head>
<meta charset="UTF-8">
<title>Tidy Wren Home and Yard – Business Card Front</title>
<link rel="stylesheet" href="https://fonts.googleapis.com/css2?family=Comfortaa:wght@600;700&family=Archivo+Narrow:wght@700&display=swap">
<style>
  :root {
    --paper: #ffffff;
    --ink: #000000;
    --honey: #f9c623;
  }
  html, body {
    margin: 0;
    padding: 0;
    width: 1200px;
    height: 1200px;
    overflow: hidden;
    background: var(--paper);
  }
  .card-face {
    position: relative;
    width: 1200px;
    height: 1200px;
    background: var(--paper);
    color: var(--ink);
  }
  .side-label {
    position: absolute;
    top: 88px;
    right: 78px;
    margin: 0;
    font-family: "Archivo Narrow", "Arial Narrow", sans-serif;
    font-weight: 700;
    font-size: 86px;
    letter-spacing: -1px;
    line-height: 1;
  }
  .brand {
    position: absolute;
    left: 0;
    right: 0;
    top: 470px;
    display: flex;
    align-items: center;
    justify-content: center;
    gap: 34px;
  }
  .brand-dot {
    width: 96px;
    height: 96px;
    border-radius: 50%;
    background: var(--honey);
    flex: none;
  }
  .brand-name {
    margin: 0;
    font-family: "Comfortaa", sans-serif;
    font-weight: 700;
    font-size: 150px;
    line-height: 1;
    letter-spacing: -2px;
    color: var(--ink);
  }
  .contact {
    position: absolute;
    top: 846px;
    margin: 0;
    font-family: "Comfortaa", sans-serif;
    font-weight: 700;
    font-size: 38px;
    line-height: 1;
    white-space: nowrap;
  }
  .contact-left { left: 108px; }
  .contact-right { right: 102px; }
  .contact-name { text-transform: capitalize; margin-right: 12px; }
</style>
</head>
<body>
  <main class="card-face">
    <h2 class="side-label">Front</h2>

    <div class="brand">
      <span class="brand-dot" aria-hidden="true"></span>
      <h1 class="brand-name">Tidy Wren</h1>
    </div>

    <p class="contact contact-left"><span class="contact-name">Mark</span>042.736.1508</p>
    <p class="contact contact-right"><span class="contact-name">Dean</span>043.968.2715</p>
  </main>
</body>
</html>
```